Design of Product Brochure

TOV Analytics Consultancy, based in Namibia, is launching a premium charcoal brand: Embera Charcoal. We manufacture two distinct, high-quality product lines: one for the serious home barbecuer and one for professional restaurant kitchens.
The objective of this project is to create a cohesive and compelling visual identity across a product brochure (for B2B sales and high-end B2C) and a marketing website. The designs must elevate Embera Charcoal from a simple commodity to a premium, trusted fuel choice, emphasizing its Namibian origin, scientific backing, and superior performance.

```html
<!DOCTYPE html>
<html lang="en">
<head>
<meta charset="utf-8">
<title>Embera Charcoal – Product Brochure</title>
<link href="https://fonts.googleapis.com/css2?family=Rubik:wght@500;700;900&family=Nunito:wght@400;600&display=swap" rel="stylesheet">
<style>
:root{
  --red:#d3302b;
  --ink:#111111;
  --charcoal:#2b2b2d;
  --grey:#f5f5f5;
  --line:#e4e4e4;
  --paper:#ffffff;
  --page:#ffffff;
}
*{box-sizing:border-box;margin:0;padding:0}
html,body{width:1200px;height:496px;overflow:hidden;background:var(--page)}
body{position:relative;font-family:"Nunito",sans-serif;color:var(--ink)}
.sheet{position:absolute;top:37px;width:546px;height:422px;background:var(--paper);box-shadow:0 0 3px rgba(0,0,0,.18);overflow:hidden}
.sheet--outside{left:39px}
.sheet--inside{left:616px}
.sheet-art{position:absolute;inset:0}
.fold{position:absolute;top:0;bottom:0;width:1px;background:var(--line)}
.abs{position:absolute}
.head{font-family:"Rubik",sans-serif;font-weight:700;font-size:12px;letter-spacing:.2px;line-height:19px;text-transform:uppercase}
.head .accent{color:var(--red)}
.red{color:var(--red)}
.body{font-size:8px;line-height:14.7px}
.about{left:18px;top:26px;width:160px}
.about .tagline{margin-top:6px;color:var(--red)}
.about .copy{margin-top:11px}
.about .copy + .copy{margin-top:11px}
.fuel{left:190px;top:24px;width:162px;text-align:center}
.fuel .copy{margin-top:4px;font-size:8.5px;line-height:16px}
.contact{left:206px;width:160px;display:flex;align-items:center;color:#fff;font-size:8px}
.contact .ring{width:21px;height:21px;border:1px solid #fff;border-radius:50%;display:flex;align-items:center;justify-content:center;margin-right:12px;flex:none}
.hero-title{right:25px;top:24px;text-align:right;font-family:"Rubik",sans-serif;font-weight:900;font-size:21px;line-height:29px;color:#fff}
.wordmark{left:396px;top:365px;display:flex;align-items:center}
.wordmark .dot{width:30px;height:30px;border-radius:50%;background:var(--charcoal);margin-right:8px}
.wordmark .name{font-family:"Rubik",sans-serif;font-weight:700;font-size:16px;line-height:16px;color:var(--red)}
.charts-title{left:0;width:182px;top:23px;text-align:center}
.compare{position:absolute;left:4px;top:57px;width:173px;border-collapse:collapse;font-size:7.8px;line-height:14px}
.compare th{background:var(--ink);color:#fff;font-family:"Rubik",sans-serif;font-weight:500;font-size:7.5px;text-align:left;vertical-align:top;padding:6px 3px 0 8px;height:38px;line-height:14px}
.compare td{background:var(--grey);vertical-align:top;padding:6px 2px 0 8px;border-top:1px solid var(--line)}
.compare td + td{border-left:1px solid var(--line)}
.compare th + th{border-left:1px solid #333}
.compare td:first-child{color:var(--red)}
.charts-note{left:10px;width:162px;top:304px;text-align:center}
.products-title{left:182px;width:182px;top:15px;text-align:center}
.product{position:absolute;left:193px;width:161px;background:#fff;border:1px solid #eee;border-radius:6px;box-shadow:0 0 4px rgba(0,0,0,.06)}
.product .icon{position:absolute;left:11px;width:24px;height:24px;border:1px solid var(--red);border-radius:50%}
.product .name{position:absolute;left:45px;font-size:9.5px;color:var(--red)}
.product .copy{position:absolute;left:13px;width:142px}
.science-head{left:376px;top:45px}
.science-sub{left:376px;top:92px;font-size:8px;color:var(--red)}
.perk{position:absolute;left:376px;width:160px;display:flex}
.perk .icon{width:23px;height:23px;border:1px solid #999;border-radius:50%;flex:none;margin-right:11px;margin-top:0px}
.perk .title{font-size:8px;line-height:14.7px;color:var(--red)}
.perk .text{font-size:8px;line-height:14.7px}
.science-note{left:376px;top:342px;width:162px}
</style>
</head>
<body>

<!-- Outside spread -->
<section class="sheet sheet--outside">
  <svg class="sheet-art" width="546" height="422" viewBox="0 0 546 422">
    <defs>
      <linearGradient id="coal" x1="0" y1="1" x2="1" y2="0">
        <stop offset="0" stop-color="#1e1e20"/>
        <stop offset=".5" stop-color="#4a4a4d"/>
        <stop offset="1" stop-color="#2a2a2c"/>
      </linearGradient>
      <linearGradient id="kitchen" x1="0" y1="0" x2="1" y2="1">
        <stop offset="0" stop-color="#d9d4cf"/>
        <stop offset=".5" stop-color="#8a6a58"/>
        <stop offset="1" stop-color="#3a2f2a"/>
      </linearGradient>
    </defs>
    <polygon points="0,120 0,170 150,320 182,300 182,260" fill="#fdf1f0"/>
    <polygon points="8,422 182,246 182,422" fill="url(#coal)" role="img" aria-label="Close-up photograph of lump charcoal pieces"/>
    <polygon points="182,247 364,64 364,373 315,422 182,422" fill="var(--charcoal)"/>
    <polygon points="364,21 541,198 364,373" fill="url(#kitchen)" role="img" aria-label="Photograph of a chef in whites cooking in a professional kitchen"/>
    <polygon points="343,0 546,0 546,203" fill="var(--red)"/>
    <polygon points="325,124 354,88 354,149" fill="var(--red)"/>
    <polygon points="217,159 242,159 228,172" fill="var(--ink)"/>
    <polygon points="193,161 222,191 193,221" fill="var(--red)"/>
    <polygon points="511,233 534,212 534,256" fill="var(--ink)"/>
    <polygon points="497,254 508,263 497,274" fill="var(--red)"/>
    <polygon points="513,282 525,270 525,291" fill="#b5b5b5"/>
  </svg>
  <div class="fold" style="left:182px"></div>
  <div class="fold" style="left:364px"></div>

  <div class="abs about">
    <h2 class="head">About <span class="accent">Embera Charcoal</span></h2>
    <p class="body tagline">Rooted in Namibia. Backed by Science. Crafted for Performance.</p>
    <p class="body copy">From the heart of Namibia’s dense hardwood forests, Embera Charcoal is produced with meticulous care and scientific precision. Developed by TOV Analytics Consultancy, our mission is simple: to transform charcoal from a common fuel into a trusted, premium-grade energy source.</p>
    <p class="body copy">Sustainably sourced, rigorously tested, and engineered for superior performance—Embera Charcoal stands apart.</p>
  </div>

  <div class="abs fuel">
    <h2 class="head">Fuel your fire with<br><span class="accent">Embera Charcoal</span></h2>
    <p class="copy">Premium Namibian Charcoal. Backed by Science. Trusted Worldwide.</p>
  </div>

  <div class="abs contact" style="top:256px">
    <span class="ring"><svg width="11" height="11" viewBox="0 0 12 12" fill="none" stroke="#fff" stroke-width="1"><circle cx="6" cy="6" r="5"/><ellipse cx="6" cy="6" rx="2.2" ry="5"/><path d="M1 6h10M2 3.5h8M2 8.5h8"/></svg></span>
    www.emberacharcoal.com
  </div>
  <div class="abs contact" style="top:295px">
    <span class="ring"><svg width="10" height="8" viewBox="0 0 10 8"><rect width="10" height="8" rx="1" fill="#fff"/><path d="M0.5 1l4.5 3.5L9.5 1" fill="none" stroke="var(--charcoal)" stroke-width="1"/></svg></span>
    sales@emberacharcoal.com
  </div>
  <div class="abs contact" style="top:335px">
    <span class="ring"><svg width="10" height="10" viewBox="0 0 10 10"><path d="M2 0.8l1.6 2.2-1 1.1a6 6 0 0 0 3.3 3.3l1.1-1 2.2 1.6-.9 1.6C5 9.4.6 5 .4 1.7z" fill="#fff"/></svg></span>
    +264 555 0142
  </div>

  <h1 class="abs hero-title">SCIENCE<br>MEETS<br>FIRE</h1>

  <div class="abs wordmark">
    <span class="dot"></span>
    <span class="name">EMBERA<br>CHARCOAL</span>
  </div>
</section>

<!-- Inside spread -->
<section class="sheet sheet--inside">
  <svg class="sheet-art" width="546" height="422" viewBox="0 0 546 422">
    <polygon points="148,422 181,389 214,422" fill="var(--red)"/>
    <polygon points="442,0 546,0 546,89" fill="var(--red)"/>
  </svg>
  <div class="fold" style="left:182px"></div>
  <div class="fold" style="left:364px"></div>

  <h2 class="abs head charts-title">Comparative <span class="accent">Charts</span></h2>
  <table class="compare">
    <thead>
      <tr><th style="width:53px">FEATURE</th><th style="width:58px">RESTAURANT GRADE</th><th>BARBECUE GRADE</th></tr>
    </thead>
    <tbody>
      <tr style="height:29px"><td>Burn Time</td><td>Very Long</td><td>Long</td></tr>
      <tr style="height:40px"><td>Heat Consistency</td><td>Professional Level</td><td>High</td></tr>
      <tr style="height:40px"><td>Smoke Output</td><td>Ultra Low</td><td>Low</td></tr>
      <tr style="height:43px"><td>Ease of Lighting</td><td>Standard</td><td>Very Easy</td></tr>
      <tr style="height:43px"><td>Flavor Enhancement</td><td>Neutral/ Controlled</td><td>Strong Aroma</td></tr>
    </tbody>
  </table>
  <p class="abs body charts-note">For restaurants, longer burn means lower cost per cook and less frequent refueling during peak hours. For home BBQ users, it means more time enjoying the barbecue and less time managing the fire.</p>

  <h2 class="abs head products-title">Embera <span class="accent">Products</span></h2>
  <article class="product" style="top:46px;height:165px">
    <span class="icon" style="top:19px"></span>
    <h3 class="name" style="top:25px">Embera Restaurant Grade</h3>
    <p class="body copy" style="top:59px">Engineered for Professional Kitchens Trusted by chefs who demand consistency, Embera Restaurant Grade charcoal is tailored for high-volume, high-performance cooking environments.</p>
  </article>
  <article class="product" style="top:225px;height:164px">
    <span class="icon" style="top:19px"></span>
    <h3 class="name" style="top:25px">Embera Barbecue Grade</h3>
    <p class="body copy" style="top:54px">Perfect for the Home Barbecue Enthusiast Embera Barbecue Grade makes every cookout a celebration. Designed to be easy to light and rich in aroma, it brings out the best in your barbecue flavors.</p>
  </article>

  <h2 class="abs head science-head">The science <span class="accent">behind<br>our charcoal</span></h2>
  <p class="abs science-sub">Why Embera Outperforms Ordinary Charcoal</p>

  <div class="perk" style="top:117px"><span class="icon" style="margin-top:4px"></span><div><p class="title">Higher Carbon Content</p><p class="text">More energy per kilogram</p></div></div>
  <div class="perk" style="top:157px"><span class="icon" style="margin-top:4px"></span><div><p class="title">Consistent Heat Output</p><p class="text">Reliable performance for chefs &amp; grillers</p></div></div>
  <div class="perk" style="top:211px"><span class="icon" style="margin-top:4px"></span><div><p class="title">Longer Burn Time</p><p class="text">Fewer refills, better efficiency</p></div></div>
  <div class="perk" style="top:250px"><span class="icon" style="margin-top:4px"></span><div><p class="title">Low Smoke, Low Ash</p><p class="text">Cleaner cooking experience</p></div></div>
  <div class="perk" style="top:290px"><span class="icon" style="margin-top:4px"></span><div><p class="title">Sustainably Produced</p><p class="text">Environmentally conscious fuel choice</p></div></div>

  <p class="abs body science-note">Our advanced carbonization process ensures every piece of Embera Charcoal delivers predictable, repeatable results.</p>
</section>

</body>
</html>
```